Online Defensive Driving Course Looking For Creativity!

Online defensive driving school looking for interesting, eye-catching multi-media (image or animated) ad options for future advertising efforts. These ads will be used in re-marketing campaigns trying to win back customers who have already visited then left the site and can include an upgrade promotional code to entice them back.

We are unsure if we would like to go with an ad that is cohesive with our branding on-site, as this creates a familiarity for the user but limits design creativity for ads. We would like to see interesting brand-cohesive options along with fun, creative, eye-catching options that might not necessarily fit with the brand image on the page.

Company is Lonestar Motor Academy at LonestarMotorAcademy.example - http://www.lonestarmotoracademy.example/defensive-driving/index.aspx?rr=dc
Product is Bluebonnet Safe Roads, which is a course used to remove points from Texas traffic tickets.

Key Ideas
(all key ideas are optional and not all need to be reflected in each ad version - use your judgement based on your ad concept)
Free Audio Upgrade - Use promo code XYZ
No Final Exam
SRB-Approved

Correct terminology for Texas is "defensive driving" and not "traffic school" or "driving school" so please use "defensive driving" in your ad.

For sizes, please choose a standard ad size - either a leaderboard size (728x90) or medium rectangle (300x250) or wide skyscraper (160x600).

Industry/Entity Type

Driving School

Font styles to use
Sans Serif

Colors

Designer to choose colors to be used in the design.

Requirements
Should not have
• "Traffic school", "driving school".

```html
<!DOCTYPE html>
<html lang="en">
<head>
<meta charset="utf-8">
<title>Lonestar Motor Academy – Remarketing Ad Set</title>
<link rel="stylesheet" href="https://fonts.googleapis.com/css2?family=Lato:wght@700;900&display=swap">
<style>
  :root {
    --stage-light: #f4f4f4;
    --stage-mid: #b9b9b9;
    --stage-dark: #4a4a4a;
    --card: #ffffff;
    --headline: #ffffff;
    --code-blue: #14b4f0;
    --cta: #fbaa0a;
    --cta-edge: #c27800;
    --brand-ink: #1e2533;
    --brand-mark: #c8102e;
    --sky: #9fb7cc;
    --foliage: #4c6d2e;
    --road: #55585e;
    --hood: #c4201b;
  }
  * { box-sizing: border-box; margin: 0; padding: 0; }
  html, body { width: 1200px; height: 804px; overflow: hidden; }
  body {
    position: relative;
    font-family: "Lato", Arial, sans-serif;
    background: radial-gradient(ellipse 70% 75% at 55% 40%, var(--stage-light) 0%, var(--stage-mid) 60%, var(--stage-dark) 100%);
  }
  .ad { position: absolute; background: var(--card); }
  .scene {
    position: absolute;
    border-bottom-right-radius: 46px;
    overflow: hidden;
  }
  .scene--tall {
    background: linear-gradient(180deg, var(--sky) 0%, #c9d6e0 30%, var(--foliage) 50%, #6f8a4a 58%, var(--road) 66%, #6a6c70 88%, var(--hood) 93%, var(--hood) 100%);
  }
  .scene--wide {
    background: linear-gradient(180deg, #a8bccb 0%, var(--foliage) 25%, #5f7b3a 45%, var(--road) 62%, #686a6e 84%, var(--hood) 90%, var(--hood) 100%);
  }
  .scene--strip {
    background: linear-gradient(90deg, #4d4f52 0%, #6a6c6f 25%, var(--road) 50%, #3f5a2a 80%, #6e5a4a 100%);
  }
  .scene--strip::after {
    content: ""; position: absolute; left: 0; right: 0; bottom: 0; height: 26%;
    background: linear-gradient(90deg, #a11a16, var(--hood) 50%, #8e1512);
  }
  .headline {
    position: absolute;
    color: var(--headline);
    font-weight: 900;
    text-align: center;
    text-transform: uppercase;
    line-height: 1.05;
    text-shadow: 0 1px 4px rgba(0,0,0,.35);
    letter-spacing: -0.2px;
  }
  .headline .code { color: var(--code-blue); }
  .cta {
    position: absolute;
    display: flex; align-items: center; justify-content: center;
    background: var(--cta);
    color: #fff;
    font-weight: 900;
    border-radius: 999px;
    box-shadow: 0 4px 0 var(--cta-edge);
    text-transform: uppercase;
  }
  .brand {
    position: absolute;
    display: flex; align-items: center;
    color: var(--brand-ink);
    font-weight: 700;
    white-space: nowrap;
  }
  .brand-mark { display: block; background: var(--brand-mark); flex: none; }

  /* wide skyscraper */
  .ad--sky { left: 50px; top: 31px; width: 192px; height: 720px; }
  .ad--sky .scene { left: 10px; top: 9px; width: 173px; height: 553px; }
  .ad--sky .headline { left: 0; right: 0; top: 110px; font-size: 27px; }
  .ad--sky .cta { left: 11px; top: 587px; width: 170px; height: 36px; font-size: 17px; }
  .ad--sky .brand { left: 0; right: 0; top: 648px; flex-direction: column; gap: 8px; font-size: 12.5px; }
  .ad--sky .brand-mark { width: 26px; height: 26px; }

  /* medium rectangle */
  .ad--rect { left: 259px; top: 328px; width: 360px; height: 300px; }
  .ad--rect .scene { left: 10px; top: 9px; width: 340px; height: 224px; }
  .ad--rect .headline { left: 0; right: 0; top: 38px; font-size: 27px; }
  .ad--rect .cta { left: 64px; top: 142px; width: 228px; height: 48px; font-size: 18px; }
  .ad--rect .brand { left: 22px; top: 246px; gap: 10px; font-size: 19px; }
  .ad--rect .brand-mark { width: 32px; height: 32px; }

  /* leaderboard */
  .ad--board { left: 259px; top: 643px; width: 874px; height: 108px; }
  .ad--board .scene { left: 367px; top: 9px; width: 495px; height: 91px; border-bottom-right-radius: 30px; }
  .ad--board .headline { left: 0; right: 0; top: 19px; font-size: 26px; z-index: 1; }
  .ad--board .cta { left: 48px; top: 45px; width: 229px; height: 48px; font-size: 18px; }
  .ad--board .brand { left: 12px; top: 6px; gap: 10px; font-size: 19px; }
  .ad--board .brand-mark { width: 32px; height: 32px; }
</style>
</head>
<body>

<section class="ad ad--sky" aria-label="Wide skyscraper ad, 160 by 600">
  <div class="scene scene--tall" role="img" aria-label="Photo: open country road lined with trees under a cloudy sky, seen over a red car hood">
    <p class="headline">Free audio<br>upgrade<br>use promo<br>code<br><span class="code">Listenfree</span></p>
  </div>
  <a class="cta">Learn more</a>
  <div class="brand"><span class="brand-mark"></span>LonestarMotorAcademy.example</div>
</section>

<section class="ad ad--rect" aria-label="Medium rectangle ad, 300 by 250">
  <div class="scene scene--wide" role="img" aria-label="Photo: tree-lined country road seen over a red car hood">
    <p class="headline">Free audio upgrade<br>use promo code<br><span class="code">Listenfree</span></p>
    <a class="cta">Learn more</a>
  </div>
  <div class="brand"><span class="brand-mark"></span>LonestarMotorAcademy.example</div>
</section>

<section class="ad ad--board" aria-label="Leaderboard ad, 728 by 90">
  <div class="brand"><span class="brand-mark"></span>LonestarMotorAcademy.example</div>
  <a class="cta">Learn more</a>
  <div class="scene scene--strip" role="img" aria-label="Photo: road ahead seen over a red car hood">
    <p class="headline">Free audio upgrade use<br>promo code <span class="code">Listenfree</span></p>
  </div>
</section>

</body>
</html>
```